Korvale the Brisden Logo/Business Card

Project MUST include a logo with business card. See attached picture.

Logo is attached to brief but I'd like to add the tagline: "What you don't know that you don't know" Logo should also have an emblem that represents the Quillon movie concept of red pill or blue pill (one in each hand). This emblem can be used with KorVale the BrisDen or without.

Two sided card

Back can have the question mark logo that is attached

I'd like the background to be black.

On side have person's info:
Doran Pelliwick
Trainer, Speaker, Author
p: 555-014-2837
e: d@korvalethebrisden.com
www.korvalethebrisden.com

Have find us on pixlo, chirvo (just logos)

Target Market(s)

People looking to know what they don't know, self development, personal growth

Industry/Entity Type

Movie

Requirements
Must have
• qr code
two sided

```html
<!DOCTYPE html>
<html lang="en">
<head>
<meta charset="utf-8">
<title>Korvale the Brisden – Business Card</title>
<link rel="stylesheet" href="https://fonts.googleapis.com/css2?family=Open+Sans:wght@400;600;700&family=EB+Garamond:wght@600&display=swap">
<style>
  :root {
    --backdrop: #e6e2dc;
    --card-white: #ffffff;
    --brand-orange: #f26a21;
    --brand-grey: #4d4d4f;
    --bar-grey: #555557;
    --ink: #2b2b2b;
    --label-red: #a3262e;
    --art-black: #141414;
  }
  * { box-sizing: border-box; margin: 0; padding: 0; }
  html, body { width: 1200px; height: 896px; overflow: hidden; }
  body { background: var(--backdrop); position: relative; font-family: "Open Sans", Arial, sans-serif; }

  .card {
    position: absolute;
    width: 692px;
    height: 395px;
    border-radius: 24px;
    box-shadow: 0 6px 14px rgba(0,0,0,0.25);
    overflow: hidden;
  }
  .card--front { left: 35px; top: 28px; background: var(--card-white); }
  .card--back { left: 435px; top: 459px; background: var(--brand-orange); }

  /* Front: brand name placeholder */
  .brand-name {
    position: absolute;
    left: 50px;
    top: 196px;
    width: 350px;
    font-family: "Open Sans", Arial, sans-serif;
    font-weight: 600;
    font-size: 30px;
    line-height: 1.2;
    color: var(--brand-grey);
    white-space: nowrap;
  }
  .tagline {
    position: absolute;
    left: 74px;
    top: 273px;
    font-family: "EB Garamond", "Times New Roman", serif;
    font-weight: 600;
    font-size: 17px;
    color: #111;
  }

  /* Front: name block */
  .name-plate {
    position: absolute;
    left: 415px;
    top: 172px;
    width: 239px;
    height: 76px;
    background: var(--brand-orange);
    color: #fff;
    padding: 10px 0 0 11px;
  }
  .name-plate__name { font-size: 25px; font-weight: 600; line-height: 1.15; }
  .name-plate__role { font-size: 14px; font-weight: 400; margin-top: 2px; }
  .name-plate__bar {
    position: absolute;
    left: 661px;
    top: 172px;
    width: 31px;
    height: 76px;
    background: var(--bar-grey);
  }

  /* Front: contact */
  .contact {
    position: absolute;
    left: 414px;
    top: 314px;
    border-left: 1px solid #e4e4e4;
    padding-left: 10px;
    list-style: none;
    font-size: 14px;
    color: var(--ink);
    line-height: 20px;
  }
  .contact__label { color: var(--label-red); font-weight: 400; display: inline-block; width: 16px; }
  .contact__item--web { font-weight: 700; }

  /* Back */
  .question-art {
    position: absolute;
    left: 257px;
    top: 42px;
    width: 181px;
    height: 203px;
    background: linear-gradient(160deg, #1e1e1e, var(--art-black));
  }
  .social {
    position: absolute;
    left: 198px;
    top: 322px;
    display: flex;
    align-items: center;
    gap: 14px;
    color: #1a1a1a;
  }
  .social__lead {
    font-family: "EB Garamond", "Times New Roman", serif;
    font-weight: 600;
    font-size: 21px;
  }
  .social__item {
    display: flex;
    align-items: center;
    gap: 6px;
    font-size: 18px;
    font-weight: 600;
  }
  .social__dot {
    width: 14px;
    height: 14px;
    border-radius: 50%;
    background: #fff;
  }
</style>
</head>
<body>

  <section class="card card--front" aria-label="Business card front">
    <h1 class="brand-name">Korvale the Brisden</h1>
    <p class="tagline">"What you don't know that you don't know"</p>

    <div class="name-plate">
      <p class="name-plate__name">Doran Pelliwick</p>
      <p class="name-plate__role">Trainer, Speaker, Author</p>
    </div>
    <div class="name-plate__bar" aria-hidden="true"></div>

    <ul class="contact">
      <li><span class="contact__label">P</span>555-014-2837</li>
      <li><span class="contact__label">E</span>d@korvalethebrisden.com</li>
      <li class="contact__item--web"><span class="contact__label">W</span>www.korvalethebrisden.com</li>
    </ul>
  </section>

  <section class="card card--back" aria-label="Business card back">
    <div class="question-art" role="img" aria-label="Typographic question mark artwork asking how deep the rabbit hole goes, on black"></div>
    <div class="social">
      <span class="social__lead">Find us on</span>
      <span class="social__item"><span class="social__dot"></span>pixlo</span>
      <span class="social__item"><span class="social__dot"></span>chirvo</span>
    </div>
  </section>

</body>
</html>
```